Hottest Internet Based Blues Radio Station in Southwest Florida All Blues 24/7 Real Authentic Blues Classic and Modern

Business

Marco "Tall Ned" Okafor
The Harbor Airwaves, Inc.
514 Willow Crest Lane
Cedar Cove, ME 33871

```html
<!DOCTYPE html>
<html lang="en">
<head>
<meta charset="utf-8">
<title>Harbor Airwaves – Business Card</title>
<link rel="stylesheet" href="https://fonts.googleapis.com/css2?family=Roboto:wght@400;500&display=swap">
<style>
  :root {
    --backdrop: #e7e4e0;
    --card-dark: #000000;
    --card-light: #ffffff;
    --accent: #c8411f;
    --ink: #333333;
    --logo-ink: #ffffff;
  }
  * { box-sizing: border-box; margin: 0; padding: 0; }
  html, body {
    width: 1200px; height: 1000px; overflow: hidden;
    background: var(--backdrop);
    font-family: "Roboto", Arial, sans-serif;
  }
  .canvas { position: relative; width: 1200px; height: 1000px; }
  .card {
    position: absolute; left: 209px; width: 782px; height: 446px;
    overflow: hidden;
  }
  .card-front { top: 41px; background: var(--card-dark); }
  .card-back { top: 511px; background: var(--card-light); }

  .brand {
    position: absolute; left: 0; right: 0; top: 100px;
    display: flex; flex-direction: column; align-items: center; gap: 36px;
  }
  .brand-mark {
    width: 160px; height: 160px; border-radius: 50%;
    border: 3px solid var(--logo-ink);
  }
  .brand-name {
    color: var(--logo-ink); font-weight: 400; font-size: 44px; line-height: 52px;
    letter-spacing: 3px; text-transform: uppercase;
  }

  .contact { position: absolute; left: 84px; top: 124px; color: var(--ink); }
  .contact-name {
    color: var(--accent); font-weight: 500; font-size: 22px; line-height: 28px; margin-bottom: 16px;
  }
  .contact-address { font-size: 17.5px; line-height: 22px; margin-bottom: 14px; }
  .contact-list { list-style: none; font-size: 17.5px; }
  .contact-list li { display: flex; align-items: center; height: 25px; }
  .contact-list svg { width: 13px; height: 13px; margin-right: 9px; fill: var(--accent); }

  .music-staff-art {
    position: absolute; right: 0; bottom: 0; width: 370px; height: 446px;
    background: radial-gradient(ellipse at 85% 75%, rgba(200,200,200,0.55), rgba(230,230,230,0.25) 55%, rgba(255,255,255,0) 80%);
  }
</style>
</head>
<body>
<div class="canvas">
  <section class="card card-front">
    <div class="brand">
      <div class="brand-mark"></div>
      <div class="brand-name">Harbor Airwaves</div>
    </div>
  </section>

  <section class="card card-back">
    <div class="music-staff-art" role="img" aria-label="Flowing music staff lines with treble clef and scattered notes in light grey"></div>
    <div class="contact">
      <h1 class="contact-name">Marco "Tall Ned" Okafor</h1>
      <p class="contact-address">The Harbor Airwaves, Inc.<br>514 Willow Crest Lane<br>Cedar Cove, ME 33871</p>
      <ul class="contact-list">
        <li><svg viewBox="0 0 16 16" aria-hidden="true"><path d="M3.6 1.2l2.3 2.9-1.3 1.6c.9 2 2.4 3.6 4.5 4.6l1.6-1.3 2.9 2.3-1.3 2.7C6.4 14.4 1.4 9.2 1 2.6z"/></svg>123-456-7890</li>
        <li><svg viewBox="0 0 16 16" aria-hidden="true"><path d="M1 3h14v1.2L8 9 1 4.2zM1 5.8l7 4.8 7-4.8V13H1z"/></svg>info@harborairwaves.com</li>
        <li><svg viewBox="0 0 16 16" aria-hidden="true"><path d="M8 1a7 7 0 100 14A7 7 0 008 1zm0 1.5c.8 0 1.7 1.6 2 4H6c.3-2.4 1.2-4 2-4zM4.6 6.5H2.7a5.5 5.5 0 012.9-3.4c-.5 1-.9 2.1-1 3.4zm6.8 0c-.1-1.3-.5-2.4-1-3.4a5.5 5.5 0 012.9 3.4zM2.7 8h1.9c.1 1.3.5 2.5 1 3.4A5.5 5.5 0 012.7 8zM6 8h4c-.3 2.4-1.2 4-2 4s-1.7-1.6-2-4zm5.4 0h1.9a5.5 5.5 0 01-2.9 3.4c.5-.9.9-2.1 1-3.4z"/></svg>www.harborairwaves.com</li>
      </ul>
    </div>
  </section>
</div>
</body>
</html>
```